Medical Practice needs a Letterhead Design

We need a clean, modern letterhead design for our stem cell medical practice.

Industry/Entity Type

Medical

```html
<!DOCTYPE html>
<html lang="en">
<head>
<meta charset="utf-8">
<title>Verantis Medical Letterhead</title>
<link rel="stylesheet" href="https://fonts.googleapis.com/css2?family=Open+Sans:ital,wght@0,400;0,600;1,400&display=swap">
<style>
  :root {
    --backdrop: #a9a9a9;
    --paper: #ffffff;
    --navy: #0f3044;
    --leaf-green: #a9c43c;
    --ink: #1f1f1f;
    --signature-tone: #d9dde0;
  }
  * { box-sizing: border-box; margin: 0; padding: 0; }
  html, body { width: 1200px; height: 1000px; overflow: hidden; }
  body {
    background: var(--backdrop);
    font-family: "Open Sans", Arial, sans-serif;
    color: var(--ink);
    position: relative;
  }
  .letterhead {
    position: absolute;
    left: 320px;
    top: 105px;
    width: 560px;
    height: 790px;
    background: var(--paper);
    box-shadow: 0 4px 14px rgba(0,0,0,0.25);
    overflow: hidden;
  }
  .brand {
    position: absolute;
    top: 58px;
    left: 0;
    width: 100%;
    text-align: center;
  }
  .brand-name {
    font-size: 30px;
    font-weight: 600;
    color: var(--navy);
    letter-spacing: -0.5px;
    line-height: 1;
  }
  .brand-sub {
    margin-top: 4px;
    font-size: 8px;
    font-weight: 600;
    color: var(--navy);
    letter-spacing: 3px;
  }
  .letter-body {
    position: absolute;
    top: 150px;
    left: 62px;
    right: 48px;
    font-size: 9.6px;
    line-height: 19px;
  }
  .salutation { margin-bottom: 28px; }
  .letter-body p.para { margin-bottom: 19px; font-style: italic; }
  .closing {
    position: absolute;
    left: 62px;
    top: 535px;
    font-size: 9.6px;
  }
  .signature {
    width: 130px;
    height: 44px;
    margin: 12px 0 10px;
    background: var(--signature-tone);
    border-radius: 3px;
  }
  .footer-rule {
    position: absolute;
    left: 0; right: 0;
    top: 700px;
    height: 5px;
    background: var(--leaf-green);
  }
  .footer {
    position: absolute;
    left: 0; right: 0;
    top: 712px;
    bottom: 0;
    background: var(--navy);
    color: #ffffff;
    font-size: 8px;
    display: flex;
    flex-direction: column;
    align-items: center;
    justify-content: center;
    gap: 7px;
  }
  .contact-row { display: flex; gap: 12px; }
  .contact-item { display: flex; align-items: center; gap: 4px; white-space: nowrap; }
  .contact-icon { width: 9px; height: 9px; display: block; }
</style>
</head>
<body>
  <main class="letterhead">
    <header class="brand">
      <div class="brand-name">Verantis</div>
      <div class="brand-sub">MEDICAL</div>
    </header>

    <section class="letter-body">
      <p class="salutation">Lorem Ipsum is simply</p>
      <p class="para">dummy text of the printing and typesetting industry. Lorem Ipsum has been the industry's standard dummy text ever since the 1500s, when an unknown printer took a galley of type and scrambled it to make a type specimen book. It has survived not only five centuries, but also the leap into electronic typesetting, remaining essentially unchanged. It was popularised in the 1960s with the release of Transfer sheets containing Lorem Ipsum passages, and more recently with desktop publishing software like Page Composer including versions of Lorem Ipsum.</p>
      <p class="para">It is a long established fact that a reader will be distracted by the readable content of a page when looking at its layout. The point of using Lorem Ipsum is that it has a more-or-less normal distribution of letters, as opposed to using 'Content here, content here', making it look like readable English. Many desktop publishing packages and web page editors now use Lorem Ipsum as their default model text, and a search for 'lorem ipsum' will uncover many web sites still in their infancy. Various versions have evolved over the years, sometimes by accident, sometimes on purpose (injected humour and the like).</p>
      <p class="para">Contrary to popular belief, Lorem Ipsum is not simply random text. It has roots in a piece of classical Latin literature from 45 BC, making it over 2000 years old. Daniel Ashford, a Latin professor at Carrowmere Institute</p>
    </section>

    <section class="closing">
      <p>Lorem Ipsum</p>
      <div class="signature" role="img" aria-label="Handwritten signature"></div>
      <p>Lorem Ipsum is a dummy</p>
    </section>

    <div class="footer-rule"></div>
    <footer class="footer">
      <div class="contact-row">
        <span class="contact-item">
          <svg class="contact-icon" viewBox="0 0 10 10"><circle cx="5" cy="5" r="5" fill="#fff"/><path d="M3 2.5l1 0 .6 1.4-.7.6a4 4 0 0 0 1.6 1.6l.6-.7 1.4.6 0 1c-2.6.4-5-2-4.5-4.5z" fill="#0f3044"/></svg>
          (000)555-0148
        </span>
        <span class="contact-item">
          <svg class="contact-icon" viewBox="0 0 10 10"><circle cx="5" cy="5" r="5" fill="#fff"/><rect x="3" y="2.5" width="4" height="5" rx=".6" fill="#0f3044"/></svg>
          (000)555-0192
        </span>
        <span class="contact-item">
          <svg class="contact-icon" viewBox="0 0 10 10"><circle cx="5" cy="5" r="5" fill="#fff"/><rect x="2.5" y="3.2" width="5" height="3.6" fill="#0f3044"/><path d="M2.5 3.2L5 5.2 7.5 3.2" stroke="#fff" stroke-width=".6" fill="none"/></svg>
          hello@verantismed.com
        </span>
      </div>
      <div class="contact-row">
        <span class="contact-item">
          <svg class="contact-icon" viewBox="0 0 10 10"><circle cx="5" cy="5" r="5" fill="#fff"/><path d="M5 8C3.3 6 3 5 3 4a2 2 0 0 1 4 0c0 1-.3 2-2 4z" fill="#0f3044"/></svg>
          420 Larkin Avenue, Suite 300, Brookfield, OR 97015
        </span>
        <span class="contact-item">
          <svg class="contact-icon" viewBox="0 0 10 10"><circle cx="5" cy="5" r="5" fill="#fff"/><circle cx="5" cy="5" r="2.6" fill="none" stroke="#0f3044" stroke-width=".7"/><path d="M2.4 5h5.2M5 2.4v5.2" stroke="#0f3044" stroke-width=".5"/></svg>
          www.verantismed.com
        </span>
      </div>
    </footer>
  </main>
</body>
</html>
```